Brackenfold's Ride for Autism 2019

we need a flyer for a fundraiser. The fundraiser is hosted by GullWink Cruisers. It will be on Sunday, April 28th, at 11am. Meet & Greet/registration will be at 11am at Marigold Autism Center (5184 Tolliver Ridge Parkway, Mishawaka, IN 46592) and ending at T.Q.W.'s Sports bar and grill. All proceeds will go to the Marigold Kinfolk Ahead Foundation. The Foundation helps special needs families with whatever they may need.

Target Market(s)

Motorcyclist

Font styles to use
Sans Serif

Colors

Designer to choose colors to be used in the design.

Requirements
Must have
• Look at Plumtree flyer. We want that kind of style.
Nice to have
• Food, drinks, DJ, 50/50 Raffle, Best Bike award, largest group award, and other amazing prizes.

```html
<!DOCTYPE html>
<html lang="en">
<head>
<meta charset="utf-8">
<title>Brackenfold's Ride for Autism 2019 – Meet &amp; Greet</title>
<link rel="stylesheet" href="https://fonts.googleapis.com/css2?family=Pirata+One&family=Dosis:wght@500;600&family=Oswald:wght@700&display=swap">
<style>
  :root {
    --ink: #ffffff;
    --deep-brown: #2a130a;
    --rust: #7a3412;
    --ember: #c0601d;
    --tire: #3a2c26;
    --black: #120a06;
  }
  html, body { margin: 0; padding: 0; overflow: hidden; background: var(--deep-brown); }
  .flyer {
    position: relative;
    width: 1200px; height: 777px;
    overflow: hidden;
    font-family: "Dosis", sans-serif;
    font-weight: 500;
    color: var(--ink);
  }
  .flyer-backdrop { position: absolute; inset: 0; }
  .fundraiser-tag {
    position: absolute;
    left: 462px; top: 516px;
    transform: translate(-50%, -50%) rotate(-65deg);
    font-family: "Oswald", sans-serif;
    font-weight: 700;
    font-size: 44px;
    letter-spacing: 16px;
    line-height: 1;
    color: var(--black);
    white-space: nowrap;
  }
  .club-name {
    position: absolute;
    left: 844px; top: 132px;
    transform: translateX(-50%);
    font-size: 20px;
    font-weight: 600;
    letter-spacing: 1px;
    line-height: 1;
    color: var(--black);
    white-space: nowrap;
  }
  .event-title {
    position: absolute;
    left: 676px; top: 176px;
    width: 340px;
    margin: 0;
    font-family: "Pirata One", cursive;
    font-weight: 400;
    color: var(--ink);
    text-shadow: 0 3px 8px rgba(0,0,0,.45);
    line-height: 1;
    white-space: nowrap;
  }
  .event-title .meet { display: block; font-size: 185px; letter-spacing: -2px; line-height: 155px; }
  .event-title .greet { display: block; font-size: 122px; letter-spacing: 1px; line-height: 110px; }
  .event-title .amp { font-family: "Dosis", sans-serif; font-weight: 600; font-size: 44px; vertical-align: 22px; margin-right: 6px; }
  .event-details p {
    position: absolute;
    left: 505px; width: 630px;
    margin: 0;
    text-align: center;
    line-height: 1;
    white-space: nowrap;
  }
  .host { top: 555px; font-size: 30px; }
  .datetime { top: 596px; font-size: 50px; letter-spacing: 0; }
  .venue {
    top: 660px; font-size: 28px;
    display: flex; align-items: center; gap: 10px;
  }
  .venue::before, .venue::after { content: ""; flex: 1; height: 1.5px; background: var(--ink); }
  .address { top: 698px; font-size: 21px; }
</style>
</head>
<body>
<main class="flyer">
  <svg class="flyer-backdrop" width="1200" height="777" viewBox="0 0 1200 777">
    <defs>
      <radialGradient id="glow" cx="0.75" cy="0.55" r="0.8">
        <stop offset="0" stop-color="#8a3d15"/>
        <stop offset="0.5" stop-color="#5a2610"/>
        <stop offset="1" stop-color="#2a130a"/>
      </radialGradient>
      <linearGradient id="photoTone" x1="0" y1="0" x2="1" y2="1">
        <stop offset="0" stop-color="#e8d89a"/>
        <stop offset="0.35" stop-color="#b58a2c"/>
        <stop offset="0.7" stop-color="#4b4a32"/>
        <stop offset="1" stop-color="#8b8a86"/>
      </linearGradient>
      <linearGradient id="stripeTone" x1="0" y1="0" x2="1" y2="0">
        <stop offset="0" stop-color="#e8801f"/>
        <stop offset="1" stop-color="#7a3412" stop-opacity="0"/>
      </linearGradient>
      <radialGradient id="disc" cx="0.35" cy="0.3" r="0.8">
        <stop offset="0" stop-color="#f4f1ee"/>
        <stop offset="0.55" stop-color="#bdb4ad"/>
        <stop offset="1" stop-color="#6f6560"/>
      </radialGradient>
    </defs>
    <rect width="1200" height="777" fill="url(#glow)"/>
    <polygon points="664,0 760,0 450,777 364,777" fill="url(#stripeTone)"/>
    <polygon points="0,0 664,0 364,777 0,777" fill="url(#photoTone)" role="img" aria-label="Photo of a motorcyclist in a helmet riding a yellow motorcycle along a sunny tree-lined road, with motion blur"/>
    <g class="wheel-frame">
      <circle cx="832" cy="290" r="264" fill="var(--tire)"/>
      <circle cx="832" cy="290" r="250" fill="none" stroke="#5e4c43" stroke-width="6"/>
      <circle cx="832" cy="290" r="226" fill="#d8cfc8"/>
      <circle cx="832" cy="290" r="214" fill="url(#disc)"/>
      <circle cx="832" cy="290" r="214" fill="none" stroke="#f7e3cc" stroke-width="3" opacity=".7"/>
    </g>
  </svg>

  <div class="fundraiser-tag">FUNDRAISER</div>

  <div class="club-name">Brackenfold United</div>

  <h1 class="event-title">
    <span class="meet">MEET</span>
    <span class="greet"><span class="amp">&amp;</span>GREET</span>
  </h1>

  <section class="event-details">
    <p class="host">hosted by GullWink Cruisers</p>
    <p class="datetime">SUN, APRIL 28, 2019 | 11:00AM</p>
    <p class="venue">Marigold Autism Center</p>
    <p class="address">5184 Tolliver Ridge Parkway,&nbsp; Mishawaka, IN 46592</p>
  </section>
</main>
</body>
</html>
```